Personal Injury Lawyer Billboard

I would like a design created featuring the image of the lawyer centered in the middle of the design.
To the left of the lawyer's image it should read "INJURED?"
To the right of the lawyer's image, it should read "CALL BRUNO!"
Under Call Bruno, include the phone number 318-555-0187.
At the bottom of the design include the lawyers information "Bruno Pemberly Accident & Injury Lawyers"
PLEASE REMOVED THE BACKGROUND IMAGERY OF THE PHOTO SUBMITTED. Also, the colors for this design should match the colors shown in the logo (navy, white and relective soft gold). Please use those color combinations in ways that best stand out.

```html
<!DOCTYPE html>
<html lang="en">
<head>
<meta charset="utf-8">
<title>Bruno Pemberly Accident &amp; Injury Lawyers – Billboard</title>
<link rel="stylesheet" href="https://fonts.googleapis.com/css2?family=Anton&family=Oswald:wght@500;600;700&display=swap">
<style>
  :root {
    --navy: #0c1f52;
    --navy-deep: #061233;
    --gold: #c9a441;
    --gold-soft: #ecd888;
    --gold-glow: rgba(201, 164, 65, 0.55);
    --white: #ffffff;
    --page: #e9ecf1;
  }
  * { margin: 0; padding: 0; box-sizing: border-box; }
  html, body {
    width: 1200px; height: 859px; overflow: hidden;
    background: var(--page);
  }
  .billboard {
    position: absolute; left: 20px; top: 140px;
    width: 1160px; height: 580px; overflow: hidden;
    background: radial-gradient(ellipse at 50% 40%, var(--navy) 0%, var(--navy-deep) 95%);
  }
  .glow {
    position: absolute; left: 290px; top: 40px; width: 580px; height: 560px;
    background: radial-gradient(ellipse at 50% 45%, var(--gold-glow) 0%, rgba(201,164,65,0.15) 55%, rgba(201,164,65,0) 72%);
  }
  .glow-corner {
    position: absolute; left: -80px; bottom: -80px; width: 300px; height: 260px;
    background: radial-gradient(ellipse at 30% 70%, rgba(201,164,65,0.45) 0%, rgba(201,164,65,0) 70%);
  }
  .portrait {
    position: absolute; left: 370px; top: 50px; width: 400px; height: 530px;
    border-radius: 150px 150px 0 0;
    background: linear-gradient(180deg, #2a2d4a 0%, #1a2660 35%, #14205a 100%);
  }
  .firm-mark {
    position: absolute; left: 28px; top: 26px; z-index: 2;
    font-family: "Oswald", sans-serif; font-weight: 500; color: var(--white);
    line-height: 1.05; letter-spacing: 0.5px; white-space: nowrap;
  }
  .firm-mark .mark-name { font-size: 28px; display: block; }
  .firm-mark .mark-tag {
    font-size: 14px; display: block; margin-top: 4px; padding-top: 4px;
    letter-spacing: 0.6px; border-top: 1px solid var(--gold);
  }
  .headline {
    position: absolute; z-index: 2; font-family: "Anton", sans-serif; font-weight: 400;
    color: var(--white); line-height: 1; letter-spacing: 1px; white-space: nowrap;
  }
  .headline--question { left: 28px; top: 175px; font-size: 96px; }
  .headline--action { right: 30px; top: 90px; font-size: 80px; }
  .phone-pill {
    position: absolute; z-index: 2; right: 30px; top: 192px; width: 420px; height: 72px;
    border-radius: 8px;
    background: linear-gradient(90deg, var(--gold) 0%, var(--gold-soft) 100%);
    font-family: "Anton", sans-serif; color: var(--navy-deep);
    font-size: 52px; line-height: 72px; text-align: center; letter-spacing: 1px; white-space: nowrap;
  }
  .signature-block {
    position: absolute; z-index: 2; left: 330px; top: 448px; width: 480px;
    text-align: center; font-family: "Oswald", sans-serif; color: var(--white); white-space: nowrap;
  }
  .signature-block .sig-name { font-size: 54px; font-weight: 700; line-height: 1; letter-spacing: 2px; }
  .signature-block .sig-rule { height: 3px; margin: 8px 20px 8px; background: var(--gold); }
  .signature-block .sig-tag { font-size: 24px; font-weight: 600; letter-spacing: 3px; line-height: 1; }
</style>
</head>
<body>
  <main class="billboard">
    <div class="glow-corner"></div>
    <div class="glow"></div>

    <div class="portrait" role="img" aria-label="Portrait of the lawyer in a navy suit and green tie, smiling with a raised fist, background removed"></div>

    <div class="firm-mark">
      <span class="mark-name">BRUNO PEMBERLY</span>
      <span class="mark-tag">ACCIDENT &amp; INJURY LAWYERS</span>
    </div>

    <h1 class="headline headline--question">INJURED?</h1>

    <h2 class="headline headline--action">CALL BRUNO!</h2>
    <div class="phone-pill">318-555-0187</div>

    <div class="signature-block">
      <div class="sig-name">BRUNO PEMBERLY</div>
      <div class="sig-rule"></div>
      <div class="sig-tag">ACCIDENT &amp; INJURY LAWYERS</div>
    </div>
  </main>
</body>
</html>
```